KQ Flier and Logo

We need a one-page color marketing consumer flier and a new logo.

Target Market(s)

Seniors

Font styles to use
Sans Serif

Colors
85acd3

Requirements
Must have
• Veteran or Military theme, Benefit amounts.

```html
<!DOCTYPE html>
<html lang="en">
<head>
<meta charset="utf-8">
<title>Veterans Benefits Flier</title>
<link href="https://fonts.googleapis.com/css2?family=Montserrat:wght@400;500;600;700;800;900&display=swap" rel="stylesheet">
<style>
  :root {
    --navy: #201d5e;
    --navy-deep: #15134a;
    --red: #b01e24;
    --red-dark: #8e1519;
    --yellow: #f3e52a;
    --white: #ffffff;
    --ink: #1f1d55;
    --muted: #6c6a9c;
    --body: #26244f;
  }
  * { margin: 0; padding: 0; box-sizing: border-box; }
  html, body { width: 703px; height: 1200px; overflow: hidden; background: var(--white); }
  body { font-family: "Montserrat", Arial, sans-serif; color: var(--body); }
  .flier { position: relative; width: 703px; height: 1200px; background: var(--white); overflow: hidden; }

  /* Header */
  .hero { position: absolute; left: 0; top: 0; width: 703px; height: 378px; }
  .hero-art {
    position: absolute; inset: 0;
    background:
      radial-gradient(ellipse at 85% 55%, rgba(176,30,36,.55) 0%, rgba(176,30,36,0) 45%),
      radial-gradient(ellipse at 15% 40%, rgba(120,118,190,.45) 0%, rgba(120,118,190,0) 55%),
      linear-gradient(180deg, #2a2770 0%, #1e1b5a 70%, #16144a 100%);
  }
  .headline {
    position: absolute; left: 0; right: 0; top: 56px; text-align: center;
    color: var(--white); font-weight: 900; font-size: 94px; line-height: 84px;
    letter-spacing: -3px; text-shadow: 0 4px 10px rgba(0,0,0,.35);
  }
  .headline span { display: block; }
  .tagline-tab { position: absolute; left: 110px; top: 266px; width: 483px; height: 58px; }
  .tagline {
    position: absolute; left: 110px; top: 273px; width: 483px; text-align: center;
    color: var(--white); font-weight: 600; font-size: 14.5px; line-height: 19px;
  }
  .cta-band {
    position: absolute; left: 0; top: 323px; width: 703px; height: 55px;
    background: var(--navy); display: flex; align-items: center; justify-content: center;
  }
  .cta { color: var(--yellow); font-weight: 800; font-size: 21px; letter-spacing: .2px; }

  /* Body columns */
  .col { position: absolute; top: 404px; }
  .col-left { left: 63px; width: 280px; }
  .col-right { left: 424px; width: 240px; }
  .divider { position: absolute; left: 352px; top: 398px; width: 1.5px; height: 160px; background: var(--navy); }
  .benefit-title { color: var(--ink); font-weight: 700; font-size: 21px; line-height: 25px; letter-spacing: .3px; }
  .benefit-note { color: var(--muted); font-size: 12.5px; line-height: 15px; margin-top: 5px; font-weight: 400; }
  .benefit-note strong { color: var(--ink); font-weight: 700; }
  .section-label {
    color: var(--red); font-weight: 800; font-size: 16px; line-height: 19px;
    text-decoration: underline; text-underline-offset: 2px; text-decoration-thickness: 1px;
  }
  .col-left .section-label { margin-top: 32px; }
  .service-list { list-style: none; margin-top: 18px; }
  .service-list li { position: relative; padding-left: 21px; font-size: 13.5px; line-height: 15px; margin-bottom: 19px; color: var(--body); width: 240px; }
  .service-list svg { position: absolute; left: 0; top: 2px; }
  .criteria .section-label { margin-top: 28px; }
  .criteria p { font-size: 13.5px; line-height: 16.5px; margin-top: 13px; color: var(--body); }

  /* Advisor & footer */
  .advisor-tab { position: absolute; left: 0; top: 990px; width: 703px; height: 84px; }
  .advisor {
    position: absolute; left: 65px; top: 998px; color: var(--white);
    font-weight: 700; font-size: 15.5px; line-height: 19px; letter-spacing: .2px;
    white-space: nowrap;
  }
  .footer {
    position: absolute; left: 0; top: 1074px; width: 703px; height: 126px;
    background: linear-gradient(180deg, var(--navy) 0%, var(--navy-deep) 100%);
  }
  .contacts { position: absolute; left: 63px; top: 22px; width: 600px; height: 34px; display: flex; align-items: center; }
  .contact { display: flex; align-items: center; gap: 7px; color: var(--white); font-weight: 600; font-size: 16px; }
  .contact-sep { width: 1.5px; height: 34px; background: rgba(255,255,255,.8); margin: 0 33px; }
  .disclaimer { position: absolute; left: 63px; top: 70px; width: 600px; color: rgba(255,255,255,.88); font-size: 9.2px; line-height: 12px; }
</style>
</head>
<body>
<main class="flier">
  <header class="hero">
    <div class="hero-art" role="img" aria-label="Waving American flag with stars and red stripes in navy and red tones"></div>
    <h1 class="headline"><span>VETERANS</span><span>BENEFITS</span></h1>
    <svg class="tagline-tab" viewBox="0 0 483 58" aria-hidden="true">
      <path d="M22 0 H461 Q472 0 476 10 L483 58 H0 L8 10 Q12 0 22 0 Z" fill="var(--red)"/>
    </svg>
    <p class="tagline">This benefit can provide a significant monthly income<br>to those who meet the eligibility requirements.</p>
    <div class="cta-band"><p class="cta">CALL TO SET UP AN APPOINTMENT TODAY!</p></div>
  </header>

  <div class="divider"></div>

  <section class="col col-left">
    <h2 class="benefit-title">MARRIED VETERAN<br>WITH CARE NEEDS:<br>UP TO $2,230 /<br>MONTH</h2>
    <p class="benefit-note">SINGLE VETERAN:<br>UP TO <strong>$1,881</strong> / MONTH</p>
    <h3 class="section-label">ELIGIBILITY REQUIREMENTS<br>SERVICE:</h3>
    <ul class="service-list">
      <li><svg width="12" height="12" viewBox="0 0 12 12"><circle cx="6" cy="6" r="6" fill="var(--navy)"/><path d="M3.2 6.2 L5.2 8 L8.8 4.2" stroke="#fff" stroke-width="1.6" fill="none"/></svg>World War I</li>
      <li><svg width="12" height="12" viewBox="0 0 12 12"><circle cx="6" cy="6" r="6" fill="var(--navy)"/><path d="M3.2 6.2 L5.2 8 L8.8 4.2" stroke="#fff" stroke-width="1.6" fill="none"/></svg>World War II</li>
      <li><svg width="12" height="12" viewBox="0 0 12 12"><circle cx="6" cy="6" r="6" fill="var(--navy)"/><path d="M3.2 6.2 L5.2 8 L8.8 4.2" stroke="#fff" stroke-width="1.6" fill="none"/></svg>Korean Conflict</li>
      <li><svg width="12" height="12" viewBox="0 0 12 12"><circle cx="6" cy="6" r="6" fill="var(--navy)"/><path d="M3.2 6.2 L5.2 8 L8.8 4.2" stroke="#fff" stroke-width="1.6" fill="none"/></svg>Vietnam Era</li>
      <li><svg width="12" height="12" viewBox="0 0 12 12"><circle cx="6" cy="6" r="6" fill="var(--navy)"/><path d="M3.2 6.2 L5.2 8 L8.8 4.2" stroke="#fff" stroke-width="1.6" fill="none"/></svg>Served in the Republic of<br>Vietnam</li>
      <li><svg width="12" height="12" viewBox="0 0 12 12"><circle cx="6" cy="6" r="6" fill="var(--navy)"/><path d="M3.2 6.2 L5.2 8 L8.8 4.2" stroke="#fff" stroke-width="1.6" fill="none"/></svg>Gulf War</li>
      <li><svg width="12" height="12" viewBox="0 0 12 12"><circle cx="6" cy="6" r="6" fill="var(--navy)"/><path d="M3.2 6.2 L5.2 8 L8.8 4.2" stroke="#fff" stroke-width="1.6" fill="none"/></svg>90 days of active duty service,<br>with at least one day during<br>war time.</li>
      <li><svg width="12" height="12" viewBox="0 0 12 12"><circle cx="6" cy="6" r="6" fill="var(--navy)"/><path d="M3.2 6.2 L5.2 8 L8.8 4.2" stroke="#fff" stroke-width="1.6" fill="none"/></svg>Discharge excluding<br>dishonorable</li>
    </ul>
  </section>

  <section class="col col-right">
    <h2 class="benefit-title">SURVIVING SPOUSE:<br>UP TO $1,209 /<br>MONTH</h2>
    <p class="benefit-note">MARRIED VETERAN ONLY SPOUSE<br>NEEDS CARE:<br>UP TO <strong>$1,442</strong> / MONTH</p>
    <div class="criteria">
      <h3 class="section-label">HEALTH:</h3>
      <p>Disabled and unable to work, or<br>65+ in need of daily assistance</p>
      <h3 class="section-label">INCOME:</h3>
      <p>Monthly income (after<br>expenses) must be below the<br>maximum benefit limit. Most<br>individuals receiving care on a<br>regular basis meet this<br>qualification</p>
      <h3 class="section-label">NET WORTH:</h3>
      <p>In 2018, KQ implemented a<br>Bright-Line Net Worth limit but<br>with proper planning most can<br>become eligible. To qualify as a<br>“surviving spouse” you had to<br>have been married to the<br>Veteran until his or her death</p>
    </div>
  </section>

  <svg class="advisor-tab" viewBox="0 0 703 84" aria-hidden="true">
    <path d="M0 0 H376 Q386 0 390 8 L411 76 H703 V84 H0 Z" fill="var(--red)"/>
  </svg>
  <p class="advisor">DALE MORROW, BENEFITS PLANNER<br>240 Elm Ave., Ste 310 Lakeview, TX<br>75510</p>

  <footer class="footer">
    <div class="contacts">
      <span class="contact">
        <svg width="15" height="15" viewBox="0 0 24 24"><path d="M6.6 10.8c1.4 2.8 3.8 5.1 6.6 6.6l2.2-2.2c.3-.3.7-.4 1-.2 1.1.4 2.3.6 3.6.6.6 0 1 .4 1 1V20c0 .6-.4 1-1 1C10.6 21 3 13.4 3 4c0-.6.4-1 1-1h3.5c.6 0 1 .4 1 1 0 1.3.2 2.5.6 3.6.1.3 0 .7-.2 1z" fill="#fff"/></svg>
        555-210-4400
      </span>
      <span class="contact-sep"></span>
      <span class="contact">
        <svg width="15" height="15" viewBox="0 0 24 24"><rect x="3" y="9" width="4" height="13" fill="#fff"/><rect x="9" y="9" width="12" height="13" fill="#fff"/><rect x="10" y="2" width="9" height="6" fill="#fff"/><rect x="11" y="12" width="2" height="2" fill="var(--navy)"/><rect x="15" y="12" width="2" height="2" fill="var(--navy)"/><rect x="11" y="16" width="2" height="2" fill="var(--navy)"/><rect x="15" y="16" width="2" height="2" fill="var(--navy)"/></svg>
        555-210-4401
      </span>
      <span class="contact-sep"></span>
      <span class="contact">
        <svg width="15" height="15" viewBox="0 0 24 24"><circle cx="12" cy="12" r="9.5" fill="none" stroke="#fff" stroke-width="2"/><ellipse cx="12" cy="12" rx="4" ry="9.5" fill="none" stroke="#fff" stroke-width="1.8"/><path d="M2.5 12h19" stroke="#fff" stroke-width="1.8"/></svg>
        www.SRPLANTX.com
      </span>
    </div>
    <p class="disclaimer">*Senior Plan Partners of Texas is a private financial services company and not part of the KQ Department.<br>Benefit is determined by the KQ based on eligibility.</p>
  </footer>
</main>
</body>
</html>
```